Professional Oral Surgery Referral Pad, Business Card, and Stationary Design

Hello,

I want to work with a designer for my startup Oral Surgery Practice called: Redmont Creek Oral Surgery & Implant Center

Ideally I would like to choose a good/professional design and work with a designer all the way to fulfill ALL of our stationary needs including referral pads, business cards, letterheads, envelopes, notepads, email signature, etc.

I would like to see designs first and hopefully would like to work with the designer for the lifetime of my practice and wanting to develop a long-term professional relationship.

In terms of the logo I have attached our practice logo files: I want to stay within the 3 colorways of the logo: Navy Blue/Silver grey/White. I would like for you to be creative and incorporate the "V" as best you can (for example greyed out watermark, etc)

I have also attached in my files the full contact info of our office in a word document: which includes address, email address, phone, fax, cell, etc.

I have also attached a few examples of double sided referral pad we can draw inspiration from. In terms of the referral pad I would ideally like to have my logo nicely placed/incorporated to make it look professional, address of the practice and contact info, my name and credentials.

Referral pad must have lines for patient, date of birth, phone number, referring doctor name, odontogram of all adult teeth and pediatric teeth, nice and big - so easy for dentist to refer. Also a jaw drawing of the intraoral cavity. Below that should have comments to surgeon.

In terms of procedures, I would like to have options of IV sedation, extractions, wisdom teeth, bone graft, pathology, tmj, trauma, expose/bond, orthognathic, other (list below)

In the back we can have a greyed out map of my practice address and Instructions for patients should include to bring insurance documentation, medication list, etc.

The final nitty gritty details of the referral pad can be worked on once I am happy with the design.

Target Market(s)

Patients who need oral surgical services and dentist referrals

Industry/Entity Type

Oral and Maxillofacial Surgery

Font styles to use
Other font styles liked:
• I would leave it up to the designers!

Colors
0054AA
0677BA
7BADD7
CADEEF
E8F1F8

Requirements
Must have
• Professional/sleek/modern and three color ways same as logo (navy blue, silver gray, and white)
Nice to have
• I would like to highlight my logo especially the implant ā€œvā€ either as watermark or part of the header or footnote. I will leave it to the expertise of the designer

```html
<!DOCTYPE html>
<html lang="en">
<head>
<meta charset="utf-8">
<title>Redmont Creek Oral Surgery – Letterhead</title>
<link href="https://fonts.googleapis.com/css2?family=Crimson+Text:wght@400;600&family=Lato:wght@700&display=swap" rel="stylesheet">
<style>
  :root {
    --backdrop: #b5b5b5;
    --paper: #ffffff;
    --navy: #00388a;
    --silver: #8c8c8c;
    --ink: #1a1a1a;
  }
  * { margin: 0; padding: 0; box-sizing: border-box; }
  html, body { width: 1200px; height: 1128px; overflow: hidden; }
  body { background: var(--backdrop); position: relative; font-family: "Crimson Text", Georgia, serif; }

  .letterhead {
    position: absolute; left: 284px; top: 144px;
    width: 633px; height: 819px;
    background: var(--paper); overflow: hidden;
  }

  .practice-address {
    position: absolute; right: 476px; top: 40px;
    font-style: normal; text-align: right; color: var(--ink);
    font-size: 11.5px; line-height: 12.4px; white-space: nowrap;
  }
  .practice-address .practice-name { font-weight: 600; text-transform: uppercase; font-size: 10.5px; }

  .divider {
    position: absolute; top: 44px; width: 2px; height: 56px; background: var(--silver);
  }
  .divider--left { left: 168px; }
  .divider--right { left: 442px; }

  .brand-name {
    position: absolute; left: 184px; top: 49px; width: 252px;
    text-align: center; color: var(--navy);
    font-size: 15px; line-height: 17px; font-weight: 400; text-transform: uppercase; letter-spacing: 0.6px;
  }

  .contact-list {
    position: absolute; left: 456px; top: 41px; list-style: none;
    font-size: 11px; line-height: 14.4px; color: var(--ink); letter-spacing: 0.4px; white-space: nowrap;
  }
  .contact-list li { display: flex; align-items: center; gap: 7px; }
  .contact-list .phone { letter-spacing: 1px; }
  .contact-list svg { width: 8px; height: 8px; fill: var(--navy); flex: none; }

  .header-rule {
    position: absolute; left: 41px; top: 113px; width: 547px; height: 2px; background: var(--silver);
  }

  .footer-band {
    position: absolute; left: 0; bottom: 0; width: 633px; height: 52px;
    background: var(--navy);
  }

  .format-label {
    position: absolute; top: 1006px; left: 0; width: 1200px; text-align: center;
    font-family: "Lato", Arial, sans-serif; font-weight: 700; font-size: 18px; letter-spacing: 2px; color: #111;
  }
</style>
</head>
<body>
  <main class="letterhead">
    <address class="practice-address">
      <div class="practice-name">Redmont Creek</div>
      <div class="practice-name">Oral Surgery</div>
      <div class="practice-name">&amp; Implant Center</div>
      <div>418 N Alder Ave</div>
      <div>Redmont, CA 91350</div>
    </address>

    <span class="divider divider--left"></span>

    <div class="brand-name">Redmont Creek<br>Oral Surgery<br>&amp; Implant Center</div>

    <span class="divider divider--right"></span>

    <ul class="contact-list">
      <li class="phone"><svg viewBox="0 0 10 10"><path d="M2 0.5 L3.6 0.5 L4.2 3 L3 3.8 C3.6 5.2 4.8 6.4 6.2 7 L7 5.8 L9.5 6.4 L9.5 8 C9.5 9 8.7 9.6 7.8 9.5 C4.2 9 1 5.8 0.5 2.2 C0.4 1.3 1 0.5 2 0.5Z"/></svg>555 204 1187</li>
      <li class="phone"><svg viewBox="0 0 10 10"><path d="M2.5 0.5h5v2.5h-5z M0.5 3.5h9v4h-1.5v-1.5h-6v1.5h-1.5z M2.5 6.5h5v3h-5z"/></svg>555 204 1190</li>
      <li><svg viewBox="0 0 10 10"><path d="M0.5 2h9v0.8l-4.5 3-4.5-3z M0.5 3.8l4.5 3 4.5-3v4.2h-9z"/></svg>info@redmontcreekos.com</li>
      <li><svg viewBox="0 0 10 10"><circle cx="5" cy="5" r="4.5"/></svg>redmontcreekos.com</li>
    </ul>

    <span class="header-rule"></span>

    <div class="footer-band" role="img" aria-label="Navy decorative footer band"></div>
  </main>

  <div class="format-label">LETTER</div>
</body>
</html>
```